Vital Spark Electrical in need of a business card design

We need a new business card designed for our electrical business. We have a logo already which I will attach below.
Would like the business card to be..
-BLACK background preferably, possibly white back ground behind logo if colours clash.
-White & Blue (logo blue) text
Something that makes the logo pop, & a modern look. Possibly minimal clean format.

REQUIRE:
-Logo on front & back

TEXT TO INCLUDE (ON ONE SIDE):

Tom Harlow
Director/Electrician
M: 0417 365 208
E:info@vitalsparkelectrical-example.com.au
W:www.vitalsparkelectrical-example.com.au
R.E.C 57318

Custom/New Homes
Renovations
Commercial Office/Shop Fit-outs
Communications & Security Cameras
Electric Vehicle Chargers
Airconditioning
Updates

Requirements
Nice to have
• Possibly even lighten the grey shades for the words 'Vital' & 'Spark' to be more easily read on a black background.

```html
<!DOCTYPE html>
<html lang="en">
<head>
<meta charset="utf-8">
<title>Vital Spark Electrical – Business Card</title>
<link rel="stylesheet" href="https://fonts.googleapis.com/css2?family=Montserrat:wght@800&family=Roboto:wght@400;500&display=swap">
<style>
  :root {
    --page: #ffffff;
    --card: #2a2a2a;
    --white: #ffffff;
    --blue: #0aa6e0;
  }
  * { margin: 0; padding: 0; box-sizing: border-box; }
  html, body { width: 1200px; height: 839px; overflow: hidden; background: var(--page); }
  body { position: relative; font-family: "Roboto", Arial, sans-serif; color: var(--white); }

  .card {
    position: absolute;
    top: 55px;
    width: 466px;
    height: 736px;
    background: var(--card);
    border-radius: 24px;
  }
  .card--front { left: 121px; }
  .card--back { left: 615px; }

  /* Front */
  .front-mark {
    position: absolute;
    left: 199px; top: 143px;
    width: 70px; height: 70px;
    background: var(--blue);
  }
  .front-rule {
    position: absolute;
    left: 181px; top: 280px;
    width: 107px; height: 2px;
    background: var(--white);
  }
  .front-name {
    position: absolute;
    left: 232px; top: 466px;
    transform: translate(-50%, -50%) rotate(90deg);
    white-space: nowrap;
    font-family: "Montserrat", Arial, sans-serif;
    font-weight: 800;
    font-size: 26px;
    line-height: 1;
    letter-spacing: 1px;
    color: var(--white);
  }

  /* Back */
  .person { position: absolute; left: 32px; top: 84px; }
  .person__name {
    font-family: "Montserrat", Arial, sans-serif;
    font-weight: 800;
    font-size: 34px;
    line-height: 1;
    letter-spacing: 0.5px;
    text-transform: uppercase;
  }
  .person__role {
    margin-top: 7px;
    font-size: 18px;
    letter-spacing: 1.8px;
    line-height: 1;
  }

  .contact { position: absolute; left: 32px; top: 184px; list-style: none; }
  .contact li { line-height: 1; white-space: nowrap; }
  .contact__licence, .contact__phone { font-size: 25px; }
  .contact__phone { margin-top: 15px; }
  .contact__email { font-size: 20px; margin-top: 10px; }
  .contact__web { font-size: 20px; margin-top: 14px; }

  .back-brand {
    position: absolute;
    left: 53px; top: 408px;
    display: flex;
    align-items: center;
    gap: 16px;
  }
  .back-brand__mark { width: 44px; height: 44px; background: var(--blue); }
  .back-brand__name {
    font-family: "Montserrat", Arial, sans-serif;
    font-weight: 800;
    font-size: 27px;
    color: var(--white);
    white-space: nowrap;
  }
  .back-rule {
    position: absolute;
    left: 99px; top: 493px;
    width: 270px; height: 2px;
    background: var(--blue);
  }

  .services { position: absolute; left: 30px; top: 513px; list-style: none; }
  .services li {
    font-size: 24.5px;
    font-weight: 500;
    line-height: 29.6px;
    white-space: nowrap;
  }
</style>
</head>
<body>
  <section class="card card--front" aria-label="Card front">
    <div class="front-mark"></div>
    <div class="front-rule"></div>
    <div class="front-name">Vital Spark Electrical</div>
  </section>

  <section class="card card--back" aria-label="Card back">
    <div class="person">
      <h1 class="person__name">Tom Harlow</h1>
      <p class="person__role">DIRECTOR/ELECTRICIAN</p>
    </div>

    <ul class="contact">
      <li class="contact__licence">R.E.C 57318</li>
      <li class="contact__phone">M: 0417 365 208</li>
      <li class="contact__email">E:&nbsp; info@vitalsparkelectrical-example.com.au</li>
      <li class="contact__web">W: www.vitalsparkelectrical-example.com.au</li>
    </ul>

    <div class="back-brand">
      <span class="back-brand__mark"></span>
      <span class="back-brand__name">Vital Spark Electrical</span>
    </div>
    <div class="back-rule"></div>

    <ul class="services">
      <li>Renovations</li>
      <li>Airconditioning</li>
      <li>Custom/New Homes</li>
      <li>Electric Vehicle Chargers</li>
      <li>Commercial Office/Shop Fit-outs</li>
      <li>Communications &amp; Security Cameras</li>
    </ul>
  </section>
</body>
</html>
```